Leaflet and introduction email. designer required

To redesign our existing leaflet to more resemble our website style. The leaflet is to be a two fold A4 leaflet / menu for perspective customers who want physical further info on our company.
Also to redesign our attached PDF document into a better design. It will be emailed as a HTML email brochure introducing our company, with design style and link to our website. Food images available in addition to what is on our website
Target Market(s)
schools, nurseries, hospitals, and offices. Also local London boroughs.
Industry/Entity Type
Catering
Font styles to use
Other font styles liked:
- Heiti SC Light or similiar
Requirements
Must have
- modern quality feel. established company.
- follow company and Logo colours primarily.
Nice to have
- see website for style and fonts. www.brightplatter.catering
Should not have
- childish fonts and clip-art. design traits of attached documents, they should look more similiar to website.

```html
<!DOCTYPE html>
<html lang="en">
<head>
<meta charset="utf-8">
<title>Summer Holiday Meals – Bright Platter Catering</title>
<link rel="stylesheet" href="https://fonts.googleapis.com/css2?family=Marcellus&family=Roboto+Condensed:wght@400;700&display=swap">
<style>
  :root {
    --green: #4cb75a;
    --green-dark: #3fa04d;
    --ink: #2b2b2b;
    --grey-band: #6d6e70;
    --white: #ffffff;
    --panel: rgba(255,255,255,0.93);
  }
  * { box-sizing: border-box; margin: 0; padding: 0; }
  html, body { width: 1200px; height: 819px; overflow: hidden; background: var(--white); }
  .leaflet { position: relative; width: 1200px; height: 819px; overflow: hidden; font-family: "Roboto Condensed", "Arial Narrow", sans-serif; color: var(--ink); }
  .backdrop {
    position: absolute; left: 25px; top: 25px; width: 1150px; height: 770px;
    background:
      radial-gradient(circle at 1150px 560px, #b9d77a 0 70px, transparent 110px),
      radial-gradient(circle at 40px 420px, #c48a5a 0 60px, transparent 100px),
      radial-gradient(circle at 1120px 330px, #d9453d 0 30px, transparent 80px),
      radial-gradient(circle at 90px 700px, #9ccf6a 0 40px, transparent 100px),
      radial-gradient(circle at 600px 790px, #8fc460 0 40px, transparent 120px),
      linear-gradient(135deg, #f3f1ec, #e9ebe3);
  }
  .panel { position: absolute; left: 40px; top: 40px; width: 1120px; height: 678px; background: var(--panel); }
  .headline { position: absolute; left: 92px; top: 92px; font-family: "Marcellus", serif; font-weight: 400; color: var(--green); font-size: 64px; line-height: 72px; }
  .intro { position: absolute; left: 90px; top: 268px; width: 445px; font-size: 17.5px; line-height: 22px; }
  .intro p { margin-bottom: 8px; }
  .slogan { position: absolute; left: 92px; top: 631px; width: 417px; height: 65px; border: 1.5px solid var(--green); padding: 7px 9px; font-family: "Marcellus", serif; color: var(--green); font-size: 20px; line-height: 24px; }
  .brand { position: absolute; left: 705px; top: 110px; width: 345px; font-family: "Marcellus", serif; color: var(--green); font-size: 46px; line-height: 50px; text-align: left; }
  .gallery { position: absolute; left: 595px; top: 275px; width: 580px; height: 175px; }
  .intro-right { position: absolute; left: 622px; top: 490px; width: 470px; font-size: 17.5px; line-height: 22px; }
  .social { position: absolute; left: 622px; top: 632px; display: flex; align-items: center; gap: 7px; }
  .social-square { width: 25px; height: 25px; border-radius: 4px; background: var(--green); }
  .hashtag { margin-left: 14px; font-weight: 700; font-size: 18px; }
  .handles { position: absolute; left: 622px; top: 678px; font-size: 17px; }
  .contact-band { position: absolute; left: 25px; top: 718px; width: 1150px; height: 52px; background: var(--grey-band); display: flex; align-items: center; justify-content: space-between; padding: 0 26px 0 67px; color: var(--white); font-weight: 700; font-size: 25px; }
  .contact-item { display: flex; align-items: center; gap: 10px; }
  .contact-item svg { width: 18px; height: 18px; }
</style>
</head>
<body>
<div class="leaflet">
  <div class="backdrop" role="img" aria-label="Photo backdrop of fresh vegetables, herbs and fruit on white wood"></div>
  <div class="panel"></div>

  <h1 class="headline">Summer<br>Holiday Meals</h1>

  <div class="intro">
    <p>Summer Holidays has finally approached us. At this time of the year it is very common for company chefs/cooks to take some well deserved time off.</p>
    <p>Nurseries often struggle to cope with the cooking at these holiday times.That’s where Bright Platter catering comes in to save the day.</p>
    <p>We deliver hot food to nurseries and businesses pre-dominantly in and around Greater London area and were expanding all the time.</p>
    <p>Give us a call to discuss our seasonal menu, prices, and availability &amp; see if we can cover your area today.</p>
    <p>With all our food prepped &amp; cooked freshly in house, You will not be disappointed!!!</p>
  </div>

  <div class="slogan">Deliciously scrumptious hot food,<br>delivered to the workplace daily Yummy.</div>

  <div class="brand">BRIGHT PLATTER<br>CATERING LTD</div>

  <svg class="gallery" viewBox="0 0 580 175" aria-hidden="false">
    <g>
      <circle cx="87" cy="87" r="78" fill="#c9b48c" role="img" aria-label="Photo of vegetable wraps with carrots and salad"/>
      <path d="M 165 87 A 78 78 0 0 1 40 150" fill="none" stroke="var(--green)" stroke-width="9"/>
      <path d="M 128 20 A 78 78 0 0 1 165 87" fill="none" stroke="var(--green)" stroke-width="9"/>
    </g>
    <g>
      <circle cx="270" cy="87" r="78" fill="#7f9a5a" role="img" aria-label="Photo of a filled sandwich with spinach salad"/>
      <path d="M 311 20 A 78 78 0 0 1 223 150" fill="none" stroke="var(--green)" stroke-width="9"/>
    </g>
    <g>
      <circle cx="455" cy="87" r="78" fill="#c79a55" role="img" aria-label="Photo of lasagne with garlic bread and spinach"/>
      <path d="M 496 20 A 78 78 0 0 1 408 150" fill="none" stroke="var(--green)" stroke-width="9"/>
    </g>
  </svg>

  <p class="intro-right">We offer an affordable friendly pro-fessional service that does not scrimp on quality. We feel that all persons should have access to great tasting food without breaking the bank - and that includes our chil-dren</p>

  <div class="social">
    <span class="social-square"></span>
    <span class="social-square"></span>
    <span class="social-square"></span>
    <span class="hashtag">#theBrightPlattercatering</span>
  </div>
  <p class="handles">Instagram:@brightplattercatering&nbsp; Twitter:@brightplatterltd</p>

  <div class="contact-band">
    <span class="contact-item">
      <svg viewBox="0 0 18 18"><rect x="0" y="0" width="18" height="18" rx="3" fill="#fff"/><path d="M5 4 l2 0 l1 3 l-1.5 1 a7 7 0 0 0 3 3 l1-1.5 l3 1 l0 2 a1 1 0 0 1-1 1 a10 10 0 0 1-8.5-8.5 a1 1 0 0 1 1-1z" fill="var(--grey-band)"/></svg>
      customerservice@brightplatter.catering
    </span>
    <span class="contact-item">
      <svg viewBox="0 0 18 18"><rect x="1" y="3" width="16" height="12" rx="2" fill="none" stroke="#fff" stroke-width="2"/><path d="M2 5 l7 5 l7-5" fill="none" stroke="#fff" stroke-width="2"/></svg>
      0203 555 0142
    </span>
    <span class="contact-item">
      <svg viewBox="0 0 18 18"><circle cx="9" cy="9" r="8" fill="#fff"/><g fill="none" stroke="var(--grey-band)" stroke-width="1.2"><ellipse cx="9" cy="9" rx="3.5" ry="7"/><line x1="2" y1="9" x2="16" y2="9"/><line x1="9" y1="2" x2="9" y2="16"/></g></svg>
      www.brightplatter.catering
    </span>
  </div>
</div>
</body>
</html>
```